Bref créative
Biz Card for a Professional Organizer
Dana Kowalt
Cutting-Edge
Room Clearing Maestro
Serving the Bay Area
info@42plumova.com
www.42plumova.com
I'd like a clean design, possibly going vertical instead of the traditional horizontal-UNLESS it is just going to look better going horizontal.
I'm open to suggestions here. I also have black and white versions of my logo if that would work well here...
black version of logo
reverse version of logo
color version

```html
<!DOCTYPE html>
<html lang="en">
<head>
<meta charset="utf-8">
<title>42 Plumova – Business Cards</title>
<link href="https://fonts.googleapis.com/css2?family=Arimo:wght@400;700&display=swap" rel="stylesheet">
<style>
  :root {
    --backdrop: #2b2b2b;
    --card: #ffffff;
    --ink: #1a1a1a;
    --teal: #2c7f9c;
    --teal-dark: #14485c;
    --teal-light: #6fb3cc;
    --shadow: rgba(0, 0, 0, 0.5);
  }
  * { margin: 0; padding: 0; box-sizing: border-box; }
  html, body {
    width: 1200px;
    height: 901px;
    overflow: hidden;
    background: var(--backdrop);
    font-family: "Arimo", Arial, sans-serif;
  }
  .stage { position: relative; width: 1200px; height: 901px; }
  .card {
    position: absolute;
    width: 540px;
    height: 308px;
    background: var(--card);
    box-shadow: 0 12px 30px var(--shadow);
    overflow: hidden;
  }
  .card--colour { left: 100px; top: 120px; }
  .card--mono { left: 560px; top: 470px; }
  .band { position: absolute; }
  .card--colour .band {
    top: 0; right: 0; width: 52px; height: 100%;
    background: linear-gradient(90deg, var(--teal-dark), var(--teal-light) 45%, var(--teal) 70%, var(--teal-dark));
  }
  .card--mono .band {
    left: 0; bottom: 0; width: 100%; height: 40px;
    background: linear-gradient(180deg, var(--teal-dark), var(--teal-light) 45%, var(--teal) 70%, var(--teal-dark));
  }
  .brand {
    position: absolute;
    left: 34px;
    top: 96px;
    width: 190px;
    display: flex;
    align-items: center;
    gap: 10px;
    font-weight: 700;
    font-size: 30px;
    line-height: 1;
  }
  .brand-dot { width: 16px; height: 16px; border-radius: 50%; flex: none; }
  .card--colour .brand { color: var(--teal); }
  .card--colour .brand-dot { background: var(--teal); }
  .card--mono .brand { color: var(--ink); top: 90px; }
  .card--mono .brand-dot { background: var(--ink); }
  .details {
    position: absolute;
    left: 248px;
    top: 40px;
    color: var(--ink);
    font-size: 15px;
    line-height: 1.3;
  }
  .card--mono .details { top: 36px; }
  .name { font-weight: 700; font-size: 16px; }
  .area { margin-top: 22px; }
  .contact { margin-top: 22px; }
  .contact-row { display: flex; }
  .contact-label { width: 58px; }
</style>
</head>
<body>
<main class="stage">
  <section class="card card--colour">
    <div class="brand"><span class="brand-dot"></span><span>42 Plumova</span></div>
    <div class="details">
      <p class="name">Dana Kowalt</p>
      <p class="title">Room Clearing Maestro</p>
      <p class="area">Serving the Bay Area</p>
      <div class="contact">
        <p class="contact-row"><span class="contact-label">Phone :</span><span>(510) 555-0142</span></p>
        <p class="contact-row"><span class="contact-label">Email :</span><span>info@42plumova.com</span></p>
        <p>www.42plumova.com</p>
      </div>
    </div>
    <div class="band"></div>
  </section>

  <section class="card card--mono">
    <div class="brand"><span class="brand-dot"></span><span>42 Plumova</span></div>
    <div class="details">
      <p class="name">Dana Kowalt</p>
      <p class="title">Room Clearing Maestro</p>
      <p class="area">Serving the Bay Area</p>
      <div class="contact">
        <p class="contact-row"><span class="contact-label">Phone :</span><span>(510) 555-0142</span></p>
        <p class="contact-row"><span class="contact-label">Email :</span><span>info@42plumova.com</span></p>
        <p>www.42plumova.com</p>
      </div>
    </div>
    <div class="band"></div>
  </section>
</main>
</body>
</html>
```